Copper Ridge Business Cards For New Startup

I am looking for you to design some business cards for a new startup https://copperridgehub.example. I have supplied logo, brand guidelines and our signatures as a guide.

We need this to reflect the brand guidelines and the website for brand consistency,

What is Copper Ridge?

Mallorca's Business Growth Community
Join your new business community full of passionate entrepreneurs who
love to solve problems and help each other grow together!

Any questions you can ask.

Target Market(s)

Business to Business

Contact Information for Business Card

These are attached (signatures) to the job

Font styles to use
Other font styles liked:
• Open Sans

Requirements
Must have
• Match design guidelines
Nice to have
• Photos of our faces so people remember us

```html
<!DOCTYPE html>
<html lang="en">
<head>
<meta charset="utf-8">
<title>Copper Ridge Business Card</title>
<link rel="stylesheet" href="https://fonts.googleapis.com/css2?family=Open+Sans:wght@400;700&display=swap">
<style>
  :root {
    --stage: #1f1f1f;
    --olive: #676300;
    --olive-deep: #5e5a00;
    --olive-soft: #716d08;
    --olive-ink: #5f5c00;
    --paper: #ffffff;
    --grey-ink: #555555;
    --tint: #f1f0e2;
  }
  * { box-sizing: border-box; margin: 0; padding: 0; }
  html, body {
    width: 1125px; height: 1200px; overflow: hidden;
    background: var(--stage);
    font-family: "Open Sans", Arial, sans-serif;
  }
  .canvas { position: relative; width: 1125px; height: 1200px; }
  .card {
    position: absolute; left: 171px; width: 826px; height: 471px;
    border-radius: 22px; overflow: hidden;
  }
  .card--front { top: 106px; background: var(--paper); }
  .card--back { top: 639px; background: var(--olive); }

  .brand-decoration {
    position: absolute; left: 10px; top: -60px; width: 800px; height: 620px;
    border-radius: 50%;
    background: radial-gradient(ellipse at center, var(--paper) 40%, var(--tint) 62%, var(--paper) 80%);
  }
  .contact {
    position: absolute; left: 0; right: 36px; top: 175px;
    text-align: center;
  }
  .contact__name {
    font-weight: 700; font-size: 31px; color: var(--olive-ink);
    letter-spacing: 0.3px; line-height: 40px;
  }
  .contact__role {
    font-size: 21px; color: var(--olive-ink); line-height: 28px;
  }
  .contact__line {
    font-size: 19px; color: var(--grey-ink); line-height: 27px;
  }
  .contact__line:first-of-type { margin-top: 6px; }
  .social {
    display: flex; justify-content: center; gap: 4px; margin-top: 10px;
  }
  .social__square {
    width: 19px; height: 19px; background: var(--olive-ink);
  }

  .pattern-field {
    position: absolute; inset: 0;
    background: linear-gradient(135deg, var(--olive-soft), var(--olive-deep));
  }
  .back-signature {
    position: absolute; right: 70px; bottom: 38px;
    text-align: right; color: var(--paper);
  }
  .back-signature__row {
    display: flex; align-items: center; justify-content: flex-end; gap: 14px;
  }
  .back-signature__name { font-size: 22px; font-weight: 700; }
  .back-signature__ring {
    width: 72px; height: 72px; border: 3px solid var(--paper); border-radius: 50%;
  }
  .back-signature__web { font-size: 19px; margin-top: 10px; }
</style>
</head>
<body>
<main class="canvas">
  <section class="card card--front">
    <div class="brand-decoration" role="img" aria-label="Large Copper Ridge brand mark decoration"></div>
    <div class="contact">
      <h1 class="contact__name">MARCUS HALE</h1>
      <p class="contact__role">Founder &amp; Growth Hacker Copper Ridge</p>
      <p class="contact__line">+34 600 555 012|mh@copperridgehub.example</p>
      <p class="contact__line">www.copperridgehub.example</p>
      <div class="social" aria-label="Social profiles">
        <span class="social__square"></span>
        <span class="social__square"></span>
        <span class="social__square"></span>
        <span class="social__square"></span>
        <span class="social__square"></span>
      </div>
    </div>
  </section>

  <section class="card card--back">
    <div class="pattern-field" role="img" aria-label="Repeating faint brand mark pattern"></div>
    <div class="back-signature">
      <div class="back-signature__row">
        <span class="back-signature__name">Copper Ridge</span>
        <span class="back-signature__ring"></span>
      </div>
      <p class="back-signature__web">www.copperridgehub.example</p>
    </div>
  </section>
</main>
</body>
</html>
```